Corporate brochure for a multinational construction company

Designing the cover pages and inside pages layout for a construction company which has operations in GCC, India etc. It has to be a very classy design. you can visit our website www.morvelta.com for more details on the company. Specific information required for the brochure design will be uploaded as needed.

Please note
1. Though the brochure will be around 80 pages, we need design of only the following
a. Cover page
b. CEOs message page
c. Introduction to sectors (Civil, Electrical, Mechanical, Infra)
d. Pages showing engineering expertise
e. Pages showing Project highlights (buildings etc)
f. Gallery pages (2 to 4 images in each page showing completed projects with a small text)
g. Key personnel (images and positions of key staff)

So design has to be done for a maximum of 7 to 10 pages. rest will be repetition.
Please use stock images with the above tip and send your designs.
g.
Updates

Project Deadline Extended
Reason: Not happy with the designs provided till now. Request all designers to once again look at the brief which is updated and submit maximum revisions. The pay is committed so we will select the best in any case. wish you all the best.

Target Market(s)

International - Current operations in the GCC, India, Srilanka

Industry/Entity Type

Construction Company

Font styles to use
Serif
Sans Serif

Requirements
Must have
• 1. A great front cover design - this may run to the back cover also
• 2. Inside page layout - to have a common theme but different styling as required
• 3. More of images and less of text - can use full page, half page or quarter page images.
• 4. Different styling and sizes for fonts for better effect.
Nice to have
• 1. A4 landscape is what we have in mind. The size can be slightly reduced so that the 80 page brochure can fit into an A4 envelope

```html
<!DOCTYPE html>
<html lang="en">
<head>
<meta charset="utf-8">
<title>Morvelta Trading &amp; Construction — Brochure Spreads</title>
<link rel="stylesheet" href="https://fonts.googleapis.com/css2?family=Crimson+Pro:wght@400;500;600&family=Open+Sans:wght@400;600&display=swap">
<style>
  :root{
    --stage:#e9e9ea;
    --ink:#2b2b2b;
    --charcoal:#232323;
    --paper:#f7f7f5;
    --green:#3f6f46;
    --gold:#ac9b58;
    --gold-deep:#8d7d3f;
    --muted:#7a7a7a;
  }
  html,body{margin:0;padding:0;width:1200px;height:1200px;overflow:hidden;background:var(--stage);}
  .stage{position:relative;width:1200px;height:1200px;}
  .spread{position:absolute;left:60px;width:1080px;height:392px;display:flex;box-shadow:0 10px 24px rgba(0,0,0,.18);}
  .spread--services{top:170px;}
  .spread--portfolio{top:640px;}
  .page{width:540px;height:392px;display:block;}
  .serif{font-family:"Crimson Pro",Georgia,serif;}
  .sans{font-family:"Open Sans",Arial,sans-serif;}
</style>
</head>
<body>
<main class="stage">

  <!-- Spread: Civil / Electrical -->
  <section class="spread spread--services">
    <svg class="page page--civil" viewBox="0 0 540 392" xmlns="http://www.w3.org/2000/svg">
      <defs>
        <linearGradient id="civilPaper" x1="0" y1="0" x2="1" y2="0">
          <stop offset="0" stop-color="#e4e4e2"/><stop offset="1" stop-color="#fbfbfa"/>
        </linearGradient>
        <linearGradient id="civilPhoto" x1="0" y1="0" x2="1" y2="1">
          <stop offset="0" stop-color="#c9dbe8"/><stop offset=".5" stop-color="#e3c79a"/><stop offset="1" stop-color="#b9ad98"/>
        </linearGradient>
      </defs>
      <rect width="540" height="392" fill="url(#civilPaper)"/>
      <polygon points="0,0 366,0 164,392 0,392" fill="url(#civilPhoto)" role="img" aria-label="Photo: engineers in hard hats reviewing plans on a construction site"/>
      <polygon points="150,392 215,278 290,392" fill="var(--gold)"/>
      <polygon points="230,296 305,296 268,392" fill="var(--gold-deep)" opacity=".85"/>
      <text x="25" y="38" class="serif" font-size="8" fill="var(--ink)">Morvelta Trading &amp; Construction LLC, Oman</text>
      <text x="320" y="104" class="serif" font-size="22" font-weight="500" fill="var(--ink)">Civil Engineering</text>
      <rect x="320" y="114" width="146" height="4" fill="var(--green)"/>
      <g class="sans" font-size="7" fill="var(--ink)">
        <text x="320" y="148">• Foundations &amp; Structures</text>
        <text x="320" y="168">• Architecture &amp; Interior</text>
        <text x="320" y="188">Design</text>
        <text x="320" y="208">• Structural Cladding &amp; Glazing</text>
        <text x="320" y="228">• Steel Structures</text>
        <text x="320" y="248">• Hi-end Finishes</text>
        <text x="320" y="268">• Generation</text>
        <text x="320" y="288">• Distribution</text>
        <text x="320" y="308">• IT &amp; Data Centers</text>
        <text x="320" y="328">• Utilities</text>
      </g>
      <line x1="300" y1="352" x2="505" y2="352" stroke="#9a9a9a" stroke-width=".6"/>
      <text x="480" y="367" class="serif" font-size="10" font-weight="600" fill="var(--ink)">20</text>
    </svg>

    <svg class="page page--electrical" viewBox="0 0 540 392" xmlns="http://www.w3.org/2000/svg">
      <defs>
        <linearGradient id="elecPhoto" x1="0" y1="0" x2="1" y2="1">
          <stop offset="0" stop-color="#8fa4b8"/><stop offset=".5" stop-color="#5c7188"/><stop offset="1" stop-color="#2f5fa8"/>
        </linearGradient>
      </defs>
      <rect width="540" height="392" fill="var(--charcoal)"/>
      <polygon points="354,0 540,0 540,392 239,392" fill="url(#elecPhoto)" role="img" aria-label="Photo: electrician checking a switchgear panel"/>
      <polygon points="232,392 272,300 320,392" fill="var(--gold)"/>
      <polygon points="270,300 330,300 300,360" fill="var(--gold-deep)" opacity=".85"/>
      <polygon points="300,228 330,228 300,280" fill="var(--gold)" opacity=".9"/>
      <text x="42" y="38" class="serif" font-size="8" fill="#ffffff">Morvelta Trading &amp; Construction LLC, Oman</text>
      <rect x="228" y="34" width="110" height="3" fill="var(--green)"/>
      <text x="42" y="104" class="serif" font-size="22" font-weight="500" fill="#ffffff">Electrical Engineering</text>
      <rect x="42" y="114" width="148" height="4" fill="var(--green)"/>
      <g class="sans" font-size="7" fill="#ffffff">
        <text x="42" y="148">• Generation</text>
        <text x="42" y="168">• Distribution</text>
        <text x="42" y="188">• IT &amp; Data Centers</text>
        <text x="42" y="208">• Utilities</text>
      </g>
      <line x1="42" y1="352" x2="250" y2="352" stroke="#444" stroke-width=".6"/>
      <text x="42" y="367" class="serif" font-size="10" fill="#3a3a3a">21</text>
    </svg>
  </section>

  <!-- Spread: Portfolio -->
  <section class="spread spread--portfolio">
    <svg class="page page--portfolio" viewBox="0 0 540 392" xmlns="http://www.w3.org/2000/svg">
      <defs>
        <linearGradient id="portPhoto" x1="0" y1="0" x2="0" y2="1">
          <stop offset="0" stop-color="#3f86d6"/><stop offset=".45" stop-color="#e9e2c8"/><stop offset="1" stop-color="#6f8a4a"/>
        </linearGradient>
      </defs>
      <rect width="540" height="392" fill="var(--charcoal)"/>
      <polygon points="0,0 218,0 120,392 0,392" fill="url(#portPhoto)" role="img" aria-label="Photo: completed institutional building with palm trees"/>
      <polygon points="218,0 316,0 208,392 120,392" fill="var(--gold)"/>
      <polygon points="218,0 270,0 228,80" fill="var(--gold-deep)" opacity=".8"/>
      <polygon points="120,392 170,300 208,392" fill="var(--gold-deep)" opacity=".85"/>
      <polygon points="316,0 540,0 540,392 208,392" fill="var(--charcoal)"/>
      <polygon points="540,290 540,392 488,392" fill="var(--gold)"/>
      <polygon points="540,340 540,392 515,392" fill="var(--gold-deep)"/>
      <text x="530" y="38" text-anchor="end" class="serif" font-size="8" fill="#d8d8d8">Morvelta Trading &amp; Construction LLC, Oman</text>
      <text x="290" y="127" class="serif" font-size="21" font-weight="500" fill="#ffffff">Portfolio</text>
      <rect x="290" y="134" width="82" height="3" fill="var(--green)"/>
      <g class="sans" font-size="6.2" fill="#ffffff">
        <text x="290" y="160">Morvelta, as an EPC company with more than</text>
        <text x="290" y="170">3 decades of experience in Oman has built</text>
        <text x="290" y="180">landmarks around the country in almost all</text>
        <text x="290" y="190">sectors.</text>
      </g>
      <line x1="210" y1="352" x2="495" y2="352" stroke="#555" stroke-width=".6"/>
      <text x="488" y="367" class="serif" font-size="10" fill="#3a3a3a">24</text>
    </svg>

    <svg class="page page--portfolio-index" viewBox="0 0 540 392" xmlns="http://www.w3.org/2000/svg">
      <defs>
        <g id="indexIcon">
          <circle r="16" fill="var(--green)"/>
          <circle r="13" fill="none" stroke="#ffffff" stroke-width=".8"/>
          <rect x="-6" y="-7" width="12" height="13" fill="none" stroke="#ffffff" stroke-width="1.3"/>
          <line x1="-2" y1="-3" x2="-2" y2="2" stroke="#ffffff" stroke-width="1.2"/>
          <line x1="2" y1="-3" x2="2" y2="2" stroke="#ffffff" stroke-width="1.2"/>
        </g>
      </defs>
      <rect width="540" height="392" fill="var(--paper)"/>
      <polygon points="0,0 88,0 0,228" fill="var(--charcoal)"/>
      <polygon points="0,340 0,392 22,392" fill="var(--gold)"/>
      <rect x="105" y="34" width="190" height="3" fill="var(--green)"/>
      <text x="305" y="38" class="serif" font-size="8" fill="var(--ink)">Morvelta Trading &amp; Construction LLC, Oman</text>
      <text x="65" y="84" class="serif" font-size="21" font-weight="500" fill="var(--ink)">Portfolio Index</text>
      <rect x="65" y="91" width="82" height="3" fill="var(--green)"/>
      <g class="index-col" transform="translate(80,0)">
        <use href="#indexIcon" y="136"/><use href="#indexIcon" y="178"/><use href="#indexIcon" y="221"/><use href="#indexIcon" y="261"/><use href="#indexIcon" y="303"/>
      </g>
      <g class="index-col" transform="translate(308,0)">
        <use href="#indexIcon" y="136"/><use href="#indexIcon" y="178"/><use href="#indexIcon" y="221"/><use href="#indexIcon" y="261"/><use href="#indexIcon" y="303"/>
      </g>
      <g class="sans" font-size="8" fill="var(--ink)">
        <text x="106" y="139">Special Projects</text>
        <text x="106" y="181">Commercial Buildings</text>
        <text x="106" y="224">Government HQ Buildings</text>
        <text x="106" y="264">Educational Institutions</text>
        <text x="106" y="306">Defence &amp; Police Complexes</text>
        <text x="334" y="139">Sports Facilities</text>
        <text x="334" y="181">Residential</text>
        <text x="334" y="224">Tourism &amp; Hospitality</text>
        <text x="334" y="264">Infrastructural Projects</text>
        <text x="334" y="306">Hospitals</text>
      </g>
      <line x1="65" y1="352" x2="520" y2="352" stroke="#9a9a9a" stroke-width=".6"/>
      <text x="70" y="367" class="serif" font-size="10" fill="var(--ink)">25</text>
    </svg>
  </section>

</main>
</body>
</html>
```